Business Card Design

Need business card design for Quality Joinery & Building Services. We would like to see designs that use black as a background with orange writing as it would stand out.

Business

KRV CONTRACTING
MARTIN COLBY
14 PELLINGTON ST
KELLARBY DOWNS
SA 5391
0498371265
krvcontracting@tramlex.com

```html
<!DOCTYPE html>
<html lang="en">
<head>
<meta charset="utf-8">
<title>KRV Contracting – Business Cards</title>
<link rel="stylesheet" href="https://fonts.googleapis.com/css2?family=PT+Sans:wght@400;700&family=Questrial&family=Great+Vibes&display=swap">
<style>
  :root {
    --page: #ffffff;
    --card: #000000;
    --orange: #ff7a12;
    --orange-soft: #ff8a2a;
    --red: #e8261c;
    --red-dark: #8a0000;
    --red-bright: #ff1a00;
    --white: #ffffff;
  }
  * { box-sizing: border-box; margin: 0; padding: 0; }
  html, body {
    width: 1200px; height: 389px; overflow: hidden;
    background: var(--page);
  }
  .sheet { position: relative; width: 1200px; height: 389px; }

  .card {
    position: absolute; top: 19px;
    width: 565px; height: 349px;
    background: var(--card); overflow: hidden;
  }
  .card--front { left: 13px; }
  .card--back { left: 622px; }

  .company {
    font-family: "PT Sans", sans-serif; font-weight: 700;
    letter-spacing: 1.5px; white-space: nowrap;
  }
  .tagline { font-family: "Great Vibes", cursive; white-space: nowrap; }
  .person {
    font-family: "PT Sans", sans-serif; font-weight: 700;
    letter-spacing: 0.5px;
  }
  .contact { font-style: normal; white-space: nowrap; }
  .brandmark-dot { width: 10px; height: 10px; border-radius: 50%; }

  /* Front card */
  .front-curve { position: absolute; left: 0; top: 0; width: 240px; height: 349px; }
  .front-edge {
    position: absolute; right: 0; top: 0; width: 20px; height: 100%;
    background: linear-gradient(90deg, var(--red-dark), var(--red-bright) 60%, var(--red-dark));
  }
  .front-brandmark {
    position: absolute; left: 20px; top: 58px; width: 150px;
    display: flex; align-items: center; justify-content: center; gap: 8px;
    font-family: "PT Sans", sans-serif; font-weight: 700;
    font-size: 34px; color: var(--white); letter-spacing: 1px;
  }
  .front-brandmark .brandmark-dot { background: var(--white); }
  .front-city {
    position: absolute; left: 0; top: 217px; width: 195px; height: 132px;
    background: linear-gradient(180deg, rgba(255,200,120,0) 0%, #ffb070 35%, #f7e7c8 75%, #6fcf4a 100%);
  }
  .front-info { position: absolute; right: 39px; top: 0; text-align: right; color: var(--orange); }
  .front-info .company { position: absolute; right: 0; top: 40px; font-size: 22px; }
  .front-info .tagline { position: absolute; right: 0; top: 72px; font-size: 23px; color: var(--orange-soft); }
  .front-contact {
    position: absolute; right: 39px; top: 190px; text-align: right;
    font-family: "Questrial", sans-serif; font-size: 21px; line-height: 23px;
    color: var(--orange);
  }
  .front-contact .person { font-size: 19px; }

  /* Back card */
  .back-band {
    position: absolute; left: 0; top: 0; width: 100%; height: 17px;
    background: linear-gradient(90deg, var(--red-dark), var(--red-bright) 35%, var(--red-bright) 65%, var(--red-dark));
  }
  .back-content { position: absolute; left: 0; top: 0; width: 100%; text-align: center; color: var(--red); }
  .back-brandmark {
    position: absolute; left: 0; right: 0; top: 58px;
    display: flex; align-items: center; justify-content: center; gap: 8px;
    font-family: "PT Sans", sans-serif; font-weight: 700; font-size: 30px;
    color: var(--red); letter-spacing: 1px;
  }
  .back-brandmark .brandmark-dot { background: var(--red); }
  .back-content .company { position: absolute; left: 0; right: 0; top: 104px; font-size: 22px; }
  .back-content .tagline { position: absolute; left: 0; right: 0; top: 133px; font-size: 23px; }
  .back-contact {
    position: absolute; left: 0; right: 0; top: 202px;
    font-family: "Questrial", sans-serif; font-size: 16px; line-height: 20px;
    color: var(--red); text-align: center; letter-spacing: 0.5px;
  }
  .back-contact .person { font-size: 15px; letter-spacing: 1px; }
  .back-skyline {
    position: absolute; left: 0; bottom: 0; width: 100%; height: 58px;
    background: linear-gradient(180deg, rgba(200,10,0,0) 0%, #d41500 35%, var(--red-bright) 75%, #ff4a10 100%);
  }
</style>
</head>
<body>
<main class="sheet">

  <section class="card card--front" aria-label="Business card front">
    <svg class="front-curve" viewBox="0 0 240 349" aria-hidden="true">
      <defs>
        <linearGradient id="frontOrange" x1="0" y1="0" x2="1" y2="1">
          <stop offset="0" stop-color="#ff2400"/>
          <stop offset="1" stop-color="#ff6a00"/>
        </linearGradient>
      </defs>
      <path d="M0 0 H123 C200 40 245 140 231 220 C226 290 210 330 205 349 H0 Z" fill="url(#frontOrange)"/>
      <path d="M123 0 C200 40 245 140 231 220 C226 290 210 330 205 349" fill="none" stroke="#ffffff" stroke-width="3"/>
    </svg>
    <div class="front-brandmark"><span class="brandmark-dot"></span>KRV</div>
    <div class="front-city" role="img" aria-label="Illustration of city high-rise buildings with green shrubs"></div>

    <div class="front-info">
      <p class="company">KRV&nbsp;&nbsp;CONTRACTING</p>
      <p class="tagline">Quality Joinery &amp; Building Services</p>
    </div>
    <address class="contact front-contact">
      <p class="person">MARTIN COLBY</p>
      <p>14 PELLINGTON ST</p>
      <p>KELLARBY DOWNS</p>
      <p>SA 5391</p>
      <p>0498371265</p>
      <p>krvcontracting@tramlex.com</p>
    </address>
    <div class="front-edge"></div>
  </section>

  <section class="card card--back" aria-label="Business card back">
    <div class="back-band"></div>
    <div class="back-content">
      <div class="back-brandmark"><span class="brandmark-dot"></span>KRV</div>
      <p class="company">KRV&nbsp;&nbsp;CONTRACTING</p>
      <p class="tagline">Quality Joinery &amp; Building Services</p>
    </div>
    <address class="contact back-contact">
      <p class="person">MARTIN COLBY</p>
      <p>14 PELLINGTON ST., KELLARBY DOWNS, SA 5391</p>
      <p>Phone 049 837 1265</p>
    </address>
    <div class="back-skyline" role="img" aria-label="Red city skyline silhouette along the bottom edge"></div>
  </section>

</main>
</body>
</html>
```